A hand soap seller needs a premium label for a new product

We need a premium label for a bottle of soap. We want to write on it:
VANTROSELLA (Name)
Hypoallergenic and antibacterial hand soap
350 ml e / 11.8 fl oz (volume, http://pimaxo.ru/7K3RtWbqmeL519)
Saint Petersburg - Russia / www.vantrosella.ru
We want to see the face of a hippopotamus in the design. Use only black and white and green for accents (the color of grass). Examples of a hippopotamus are shown in the photo. Our soap is hypoallergenic. Ideal for both children and adults. Therefore, the label should appeal to adults and children.
The bottle will be white, and the soap dispenser will be black.
So I'm attaching an example of a soap design that we liked
Label size: height-78 mm, width-102 mm !!!

Target Market(s)

Mothers and children

Industry/Entity Type

Hand soap

Font styles to use
Serif

Colors

Designer to choose only greyscale colors for use in the design.

Requirements
Must have
• The face of a hippopotamus emerging from the grass, Black and white palette with elements of green (grass color)
Nice to have
• The face of a hippopotamus emerging from the grass
Should not have
• Different colors

```html
<!DOCTYPE html>
<html lang="en">
<head>
<meta charset="utf-8">
<title>Vantrosella Hand Soap Label</title>
<link href="https://fonts.googleapis.com/css2?family=Righteous&family=Roboto+Condensed:wght@300;700&display=swap" rel="stylesheet">
<style>
  :root {
    --label-bg: #353334;
    --ink-light: #e8e9eb;
    --mark-fill: #4d4b4c;
  }
  html, body {
    margin: 0;
    padding: 0;
    width: 1200px;
    height: 1000px;
    overflow: hidden;
    background: var(--label-bg);
  }
  .label {
    position: relative;
    width: 1200px;
    height: 1000px;
    background: var(--label-bg);
    color: var(--ink-light);
    text-align: center;
  }
  .label > * {
    position: absolute;
    left: 0;
    right: 0;
    margin: 0;
  }
  .brand-square {
    top: 113px;
    left: 447px;
    right: auto;
    width: 306px;
    height: 293px;
    background: var(--mark-fill);
  }
  .brand-name {
    top: 423px;
    font-family: "Righteous", sans-serif;
    font-weight: 400;
    font-size: 74px;
    line-height: 74px;
    letter-spacing: 1px;
  }
  .product-type {
    top: 509px;
    font-family: "Roboto Condensed", sans-serif;
    font-weight: 700;
    font-size: 32px;
    line-height: 38px;
    letter-spacing: 0.5px;
  }
  .origin {
    top: 717px;
    font-family: "Roboto Condensed", sans-serif;
    font-weight: 300;
    font-size: 32px;
    line-height: 39px;
  }
  .volume {
    top: 834px;
    font-family: "Roboto Condensed", sans-serif;
    font-weight: 700;
    font-size: 44px;
    line-height: 48px;
  }
</style>
</head>
<body>
  <main class="label">
    <div class="brand-square" aria-hidden="true"></div>

    <h1 class="brand-name">VANTROSELLA</h1>

    <p class="product-type">Hypoallergenic<br>And<br>Antibacterial Hand Soap</p>

    <p class="origin">Saint Petersburg - Russia<br>www.vantrosella.ru</p>

    <p class="volume">350 ml e / 11.8 fl oz</p>
  </main>
</body>
</html>
```